Podcast cover for Vexora

Hi
I am after a podcast cover for Vexora.The image will have to meet their guidelines
Check out images on Vexora podcast section if you are not sure. Here is what they say about specs required.
-------------------Quorbel Description below this line ----------
Cover art must be in the JPEG or PNG file formats and in the RGB color space with a minimum size of 1400 x 1400 pixels and a maximum size of 2048 x 2048 pixels. Note that these requirements are different from the standard RSS image tag specification.
Potential subscribers will see your cover art in varying sizes depending on the device they’re using. Make sure your design is effective at both its original size and at thumbnail size.
-------------------Quorbel Description above this line ----------

I will try to convey what the show is about to assist in prompting some ideas.

I am sure you have heard the expression “connecting the dots”
My podcast is a variation of this.

My show is called “holding quiet lanterns”
Just those three words to appear on the image. Remember they must be clearly readable at the size that Vexora will scale them to. (see above)

The idea behind the show is that we can create our dots and as we move through life we reach out and connect to those dots.

We are looking at the categories of Mysticism – Spirituality – Personal growth - Success

The image should reflect the above categories (absolutely not ‘godly’) and no cliché images of rising suns – halos – rainbows etc

Dots might make up some part of the image or something that represents dots. Mountains - crashing waves - jungle - Think – Nature – connected to earth – spirituality.

Some personal background which may help with the design idea. I am 55 years old and have for most of my life been searching.
Why are we here – what is our role and how do we make this life a meaningful one.

Some months ago I travelled to Iquitos, in Peru (the most remote city on the planet.) I ended up meeting a shaman and taking part in a ceremony deep in the Amazon jungle.
As a result of this I found the answers my questions. Hence the podcast to relay my experience.

Ok thats the story what can you come up with :-)

```html
<!DOCTYPE html>
<html lang="en">
<head>
<meta charset="utf-8">
<title>Holding Quiet Lanterns — Vexora Podcast Cover</title>
<link rel="stylesheet" href="https://fonts.googleapis.com/css2?family=Jost:ital,wght@1,400&display=swap">
<style>
  :root {
    --paper: #ffffff;
    --ink: #0a0a0a;
    --blue-bright: #1400ff;
    --blue-mid: #0b00a6;
    --blue-core: #04004e;
    --ribbon-tone: #ececec;
  }
  html, body {
    margin: 0;
    padding: 0;
    overflow: hidden;
    background: var(--paper);
  }
  .cover {
    position: relative;
    width: 1200px;
    height: 1200px;
    background: var(--paper);
    overflow: hidden;
  }
  .cross-field {
    position: absolute;
    inset: 0;
    width: 1200px;
    height: 1200px;
  }
  .cross-band { fill: url(#band-tone); }
  .band-stop--end { stop-color: var(--blue-bright); }
  .band-stop--mid { stop-color: var(--blue-mid); }
  .band-stop--core { stop-color: var(--blue-core); }

  .ribbon {
    position: absolute;
    top: 386px;
    width: 206px;
    height: 488px;
    background: linear-gradient(180deg, var(--paper) 0%, var(--ribbon-tone) 50%, var(--paper) 100%);
    border-radius: 40px;
  }
  .ribbon--left  { left: 34px; }
  .ribbon--right { left: 960px; }

  .title-word {
    position: absolute;
    margin: 0;
    font-family: "Jost", "Futura", sans-serif;
    font-style: italic;
    font-weight: 400;
    font-size: 142px;
    line-height: 1;
    color: var(--ink);
    white-space: nowrap;
    transform: translateX(-50%);
  }
  .title-word--first  { top: 81px;  left: 592px; }
  .title-word--second { top: 822px; left: 600px; }
  .title-word--third  { top: 977px; left: 598px; }
</style>
</head>
<body>
  <main class="cover">
    <svg class="cross-field" viewBox="0 0 1200 1200" role="img" aria-label="Diagonal cross of rounded blue dots deepening to navy at the centre">
      <defs>
        <linearGradient id="band-tone" x1="0" y1="0" x2="1" y2="0">
          <stop offset="0" class="band-stop--end"/>
          <stop offset="0.35" class="band-stop--mid"/>
          <stop offset="0.5" class="band-stop--core"/>
          <stop offset="0.65" class="band-stop--mid"/>
          <stop offset="1" class="band-stop--end"/>
        </linearGradient>
      </defs>
      <g transform="translate(596 596)">
        <rect class="cross-band" x="-750" y="-62" width="1500" height="124" rx="62" transform="rotate(45)"/>
        <rect class="cross-band" x="-750" y="-62" width="1500" height="124" rx="62" transform="rotate(-45)"/>
      </g>
    </svg>

    <div class="ribbon ribbon--left" role="img" aria-label="Line drawing of flowing wavy ribbons falling from a short horizontal bar"></div>
    <div class="ribbon ribbon--right" role="img" aria-label="Mirrored line drawing of flowing wavy ribbons falling from a short horizontal bar"></div>

    <h1 class="title-word title-word--first">Holding</h1>
    <p class="title-word title-word--second">Quiet</p>
    <p class="title-word title-word--third">Lanterns</p>
  </main>
</body>
</html>
```